Coral Wirelink Business Card

Hi, We need business cards for our sales agents for our business.
Please have a look at the website www.coralwirelink.co and also the attached files for some design expectation and different type of content to be placed on the card.
e.g. Job designation could be - Agent, Zoning Agent or Director. When you submit mock up please submit with variations in the data. Please provide fresh designs and let me know if any questions. Thanks

Industry/Entity Type

Business

```html
<!DOCTYPE html>
<html lang="en">
<head>
<meta charset="utf-8">
<title>Coral Wirelink Business Card</title>
<link rel="stylesheet" href="https://fonts.googleapis.com/css2?family=Exo+2:wght@500;600&display=swap">
<style>
  :root {
    --navy: #17213f;
    --grey-text: #9a9a9c;
    --grey-stripe: #a3a3a6;
    --card: #fbfbf9;
    --backdrop: #e4e2de;
    --url: #c9ccd6;
  }
  html, body {
    margin: 0;
    width: 1200px;
    height: 800px;
    overflow: hidden;
    background: var(--backdrop);
  }
  .card {
    position: absolute;
    left: 100px;
    top: 110px;
    width: 1000px;
    height: 580px;
    background: var(--card);
    box-shadow: 0 6px 24px rgba(0,0,0,0.12);
    overflow: hidden;
  }
  .card-band {
    position: absolute;
    inset: 0;
  }
  .brand-name {
    position: absolute;
    left: 0;
    top: 222px;
    width: 520px;
    text-align: center;
    font-family: "Exo 2", sans-serif;
    font-weight: 600;
    font-size: 44px;
    line-height: 1;
    color: var(--navy);
  }
  .divider {
    position: absolute;
    left: 520px;
    top: 48px;
    width: 1px;
    height: 290px;
    background: var(--grey-stripe);
  }
  .contact {
    position: absolute;
    left: 548px;
    top: 48px;
    font-family: "Exo 2", sans-serif;
    font-weight: 500;
    font-size: 27px;
    line-height: 1.3;
    color: var(--grey-text);
  }
  .contact p { margin: 0; }
  .contact-name {
    font-weight: 600;
    color: var(--navy);
  }
  .contact-address { margin-top: 38px !important; }
  .contact-lines { margin-top: 34px; }
  .contact-label {
    display: inline-block;
    width: 110px;
    font-weight: 600;
    color: var(--navy);
  }
  .card-url {
    font-family: "Exo 2", sans-serif;
    font-size: 28px;
    letter-spacing: 7px;
    fill: var(--url);
  }
</style>
</head>
<body>
  <div class="card">
    <svg class="card-band" width="1000" height="580" viewBox="0 0 1000 580" aria-hidden="true">
      <path d="M0,548 Q520,470 1000,318" fill="none" stroke="var(--grey-stripe)" stroke-width="10"/>
      <path d="M60,580 Q560,500 1000,356 L1000,580 Z" fill="var(--navy)"/>
      <text class="card-url" transform="translate(470 548) rotate(-13)">www.coralwirelink.co</text>
    </svg>

    <div class="brand-name">Coral Wirelink</div>

    <div class="divider"></div>

    <div class="contact">
      <p class="contact-name">Your Name</p>
      <p>Director</p>
      <p class="contact-address">4120 208th Ave NE<br>Sample, WA Address</p>
      <div class="contact-lines">
        <p><span class="contact-label">Phone:</span>425 555 0147</p>
        <p><span class="contact-label">Email:</span>Coralwire.net</p>
      </div>
    </div>
  </div>
</body>
</html>
```